Conveyancing Brochure

I am after a 4 page brochure for our Conveyancing division in our law firm Brantford Wylie Osgood Lawyers.

We are a diverse range of energetic, dynamic and innovative professionals who strive to be at the forefront of progressive legal service. Please refer to our website for more information: www.bwolegal.com.au

I would like to see the colours of our logo & also some images incorporated throughout the brochure (however I don't want it to look 'too busy' either).

The images can be based around the range of services that we provide eg: residential, development etc.

Thank you,
Maris

```html
<!DOCTYPE html>
<html lang="en">
<head>
<meta charset="utf-8">
<title>Brantford Wylie Osgood Lawyers – Conveyancing</title>
<link href="https://fonts.googleapis.com/css2?family=Questrial&family=Raleway:wght@200;400&display=swap" rel="stylesheet">
<style>
  :root {
    --teal: #29a9c4;
    --teal-light: #45bdd3;
    --ink: #3c3d40;
    --grey: #6e6f72;
    --paper: #ffffff;
    --night-top: #0e1a35;
    --night-mid: #27324d;
    --night-warm: #8a5a2c;
  }
  * { margin: 0; padding: 0; box-sizing: border-box; }
  html, body { width: 845px; height: 1200px; overflow: hidden; background: var(--paper); }
  .page {
    position: relative;
    width: 845px; height: 1200px;
    background: var(--paper);
    font-family: "Questrial", "Century Gothic", sans-serif;
    color: var(--grey);
  }
  .brand {
    position: absolute; top: 52px; left: 540px;
    display: flex; align-items: center; gap: 14px;
  }
  .brand-name {
    font-size: 25px; line-height: 28px; color: var(--ink);
  }
  .brand-mark { width: 22px; height: 22px; background: var(--teal); }
  .title {
    position: absolute; top: 210px; left: 548px;
    font-family: "Raleway", sans-serif; font-weight: 200;
    font-size: 112px; color: var(--teal-light); letter-spacing: 1px;
  }
  .intro { position: absolute; top: 352px; left: 34px; width: 470px; }
  .heading {
    font-size: 27px; color: var(--teal); margin-bottom: 8px; font-weight: 400;
  }
  .intro p { font-size: 15.5px; line-height: 27px; }
  .services { position: absolute; top: 577px; left: 34px; width: 480px; }
  .services ul { list-style: none; margin-top: 6px; }
  .services li {
    position: relative; padding-left: 44px;
    font-size: 15.5px; line-height: 20px; min-height: 37.5px;
  }
  .services li::before {
    content: ""; position: absolute; left: 4px; top: 4px;
    width: 12px; height: 12px; border-radius: 50%; background: var(--teal);
  }
  .photo {
    position: absolute; left: 537px; top: 622px; width: 308px; height: 578px;
    background:
      radial-gradient(ellipse at 45% 40%, rgba(214,150,70,.55), transparent 55%),
      linear-gradient(180deg, var(--night-top) 0%, var(--night-mid) 55%, var(--night-warm) 78%, var(--night-top) 100%);
  }
</style>
</head>
<body>
<main class="page">
  <header class="brand">
    <div class="brand-name">Brantford Wylie<br>Osgood Lawyers</div>
    <span class="brand-mark"></span>
  </header>

  <h1 class="title">What</h1>

  <section class="intro">
    <h2 class="heading">What is conveyancing?</h2>
    <p>Simply put, conveyancing is the legal process in transferring title between two or more parties. There are a few steps involved between signing the contract and settlement, and you will need the right people to guide you along the way. Whether you are buying or selling, our team of experienced lawyers can help.</p>
  </section>

  <section class="services">
    <h2 class="heading">Services</h2>
    <ul>
      <li>Preparation of contracts</li>
      <li>Pre-contractual review of contract</li>
      <li>Advice on terms of the contract</li>
      <li>Negotiate terms with the vendor/purchaser</li>
      <li>Advise you as to various searches required and obtain searches on your behalf</li>
      <li>Communicate with your lender or broker to ensure finance is ready for settlement</li>
      <li>Attend to exchange of contracts</li>
      <li>Advise in relation to mortgage documents</li>
      <li>Preparation of transfer documents</li>
      <li>Liaising with your lender and the agent</li>
      <li>Calculation of settlement adjustments</li>
      <li>Preparing and attending settlement</li>
      <li>Communicating and keeping you updated on the progress of your matter</li>
    </ul>
  </section>

  <div class="photo" role="img" aria-label="City riverside at night with a lit hotel tower and reflections on the water"></div>
</main>
</body>
</html>
```